design double sided business cards - construction

************NO IMAGES OF HOME BUILDING************ONLY IMAGES OF HOME REPAIRS*****

Front -
[ WE SOLVE ALL YOUR REPAIR NEEDS] Dwelling&Lodging
Dorian Pellham - Owner

FOR A FREE QUOTE - Call 555.314.8826
DORIANPELLHAM047@[login to view URL]
[login to view URL]

(((include home repairs/landscaping imagery on the front)))

Back -
THE CORNERSTONE FIXERS - DWELLINGS&LODGING

PLUMBING -------- FLOORING
ELECTRICAL ---------- PAINTING
LANDSCAPING ----------- DRY WALL

WE CAN HELP | HOME REPAIR | MADE EASY!

GET YOUR FREE QUOTE TODAY! Call 555.314.8826

(((include imagery of home repairmen/landscapers on the back)))

You dont have to use the attached images, those are just examples

***FINAL FILES MUST BE 300DPI CMYK LAYERED PSD FILES WITH EDITABLE TEXT***
**SIZE IS US STANDARD 2X3.5 WITH AN EXTRA 0.125 ADDED TO WIDTH AND LENGTH FOR BLEED**

```html
<!DOCTYPE html>
<html lang="en">
<head>
<meta charset="utf-8">
<title>The Cornerstone Fixers – Business Card</title>
<link rel="stylesheet" href="https://fonts.googleapis.com/css2?family=Arimo:wght@400;700&family=Tinos:wght@400;700&display=swap">
<style>
  :root {
    --backdrop: #5b5b5b;
    --green: #4a9a1c;
    --green-light: #7cc242;
    --green-dark: #2f7a12;
    --ink: #111111;
    --white: #ffffff;
    --accent-yellow: #f4ec1c;
    --sans: "Arimo", Arial, sans-serif;
    --serif: "Tinos", "Times New Roman", serif;
  }
  * { margin: 0; padding: 0; box-sizing: border-box; }
  html, body { width: 1200px; height: 1200px; overflow: hidden; background: var(--backdrop); }
  .card { position: absolute; left: 255px; width: 690px; height: 394px; overflow: hidden; }
  .card-back { top: 167px; }
  .card-front { top: 621px; }
  .card svg.art { position: absolute; inset: 0; width: 100%; height: 100%; }

  /* back side */
  .back-text { position: absolute; left: -20px; width: 690px; text-align: center; font-family: var(--sans); color: var(--ink); }
  .company-name { top: 106px; font-weight: 700; font-size: 29px; letter-spacing: 0.3px; }
  .company-sub { top: 145px; font-size: 23px; }
  .service-list { top: 196px; font-size: 15px; line-height: 21.5px; }
  .help-line { top: 278px; font-size: 19px; }
  .quote-line { top: 306px; font-size: 15px; }

  /* front side */
  .owner-name { position: absolute; left: 67px; top: 69px; font-family: var(--serif); font-size: 23px; color: var(--ink); }
  .owner-role { position: absolute; left: 67px; top: 100px; font-family: var(--serif); font-size: 17px; color: #333; }
  .contact-list { position: absolute; left: 66px; top: 230px; list-style: none; }
  .contact-item { display: flex; align-items: center; height: 30.5px; font-family: var(--serif); font-size: 14px; color: #222; white-space: nowrap; }
  .contact-item svg { width: 26px; height: 26px; margin-right: 8px; flex: none; }
  .badge-text { position: absolute; left: 399px; top: 94px; width: 220px; text-align: center; font-family: var(--serif); color: var(--white); font-size: 24px; line-height: 31.5px; }
  .badge-sub { display: block; font-family: var(--sans); color: var(--accent-yellow); font-size: 15px; line-height: 22px; margin-top: 2px; }
</style>
</head>
<body>

<section class="card card-back" aria-label="Card back">
  <svg class="art" viewBox="0 0 690 394">
    <defs>
      <linearGradient id="yard-tone" x1="0" y1="0" x2="1" y2="1">
        <stop offset="0" stop-color="#c9d3b8"/>
        <stop offset="0.5" stop-color="#a8bd8a"/>
        <stop offset="1" stop-color="#cfd6c6"/>
      </linearGradient>
      <linearGradient id="swoosh-green" x1="0" y1="0" x2="1" y2="1">
        <stop offset="0" stop-color="#7cc242"/>
        <stop offset="1" stop-color="#3d8f17"/>
      </linearGradient>
    </defs>
    <rect width="690" height="394" fill="url(#yard-tone)" role="img" aria-label="Photo of a landscaper digging in a green garden with a truck behind"/>
    <path class="swoosh" d="M330 20 C470 -10 640 10 690 60 L690 394 L560 394 C640 300 640 150 560 80 C500 35 420 20 330 20 Z" fill="url(#swoosh-green)" opacity="0.9"/>
    <path class="swoosh" d="M0 360 C180 380 420 370 560 300 C620 260 640 200 610 140 C650 220 640 330 520 394 L0 394 Z" fill="url(#swoosh-green)"/>
    <path class="swoosh-grey" d="M330 20 C420 0 520 2 600 30 C520 14 420 18 340 40 Z" fill="#8f8f8f" opacity="0.7"/>
    <rect class="title-band" x="0" y="87" width="690" height="96" fill="#ffffff" opacity="0.55"/>
    <ellipse cx="300" cy="210" rx="270" ry="160" fill="#ffffff" opacity="0.25"/>
  </svg>
  <div class="back-text company-name">THE CORNERSTONE FIXERS</div>
  <div class="back-text company-sub">Dwelling &amp; Lodging</div>
  <div class="back-text service-list">PLUMBING - FLOORING<br>ELECTRICAL - PAINTING<br>LANDSCAPING - DRY WALL</div>
  <div class="back-text help-line">WE CAN HELP | HOME REPAIR | LANDSCAPING</div>
  <div class="back-text quote-line">GET YOUR FREE QUOTE TODAY! Call 555.314.8826</div>
</section>

<section class="card card-front" aria-label="Card front">
  <svg class="art" viewBox="0 0 690 394">
    <defs>
      <radialGradient id="paper" cx="0.4" cy="0.45" r="0.8">
        <stop offset="0" stop-color="#ffffff"/>
        <stop offset="1" stop-color="#c8c8c8"/>
      </radialGradient>
      <linearGradient id="wood-tone" x1="0" y1="0" x2="1" y2="1">
        <stop offset="0" stop-color="#c9894a"/>
        <stop offset="1" stop-color="#9a5d2c"/>
      </linearGradient>
      <radialGradient id="badge-green" cx="0.45" cy="0.4" r="0.7">
        <stop offset="0" stop-color="#5aa820"/>
        <stop offset="1" stop-color="#2f7a12"/>
      </radialGradient>
    </defs>
    <rect width="690" height="394" fill="url(#wood-tone)" role="img" aria-label="Photo of hand tools on a wooden workbench: hammer, wrench, brush, tape measure, nails"/>
    <path class="paper-panel" d="M0 0 L390 0 C470 80 470 300 360 394 L0 394 Z" fill="url(#paper)"/>
    <path class="swoosh-grey" d="M240 0 L410 0 C490 80 490 300 380 394 L362 394 C472 300 470 80 390 6 C340 3 290 1 240 0 Z" fill="#9a9a9a" opacity="0.85"/>
    <path class="swoosh-white" d="M410 0 L422 0 C502 85 500 300 392 394 L378 394 C488 300 490 85 410 0 Z" fill="#ffffff"/>
    <circle class="badge" cx="512" cy="155" r="111" fill="url(#badge-green)" opacity="0.95"/>
  </svg>
  <div class="owner-name">DORIAN PELLHAM</div>
  <div class="owner-role">Owner</div>
  <ul class="contact-list">
    <li class="contact-item">
      <svg viewBox="0 0 26 26" aria-hidden="true"><circle cx="13" cy="13" r="13" fill="var(--green-light)"/><path d="M9 7c1 0 2 2.5 2 3s-1.2 1-1 1.6c.6 1.6 1.8 2.8 3.4 3.4.6.2 1.1-1 1.6-1s3 1 3 2-1.5 2.2-2.6 2C11 17 9 14.4 8 10.6 7.7 9 8 7 9 7z" fill="#fff"/></svg>
      FOR A FREE QUOTE - CALL 555.314.8826
    </li>
    <li class="contact-item">
      <svg viewBox="0 0 26 26" aria-hidden="true"><circle cx="13" cy="13" r="13" fill="var(--green-light)"/><rect x="7" y="8.5" width="12" height="9" rx="1" fill="#fff"/><path d="M7.5 9l5.5 4.5L18.5 9" fill="none" stroke="var(--green-light)" stroke-width="1.3"/></svg>
      DORIANPELLHAM047@FIXMAIL.COM
    </li>
    <li class="contact-item">
      <svg viewBox="0 0 26 26" aria-hidden="true"><circle cx="13" cy="13" r="13" fill="var(--green-light)"/><circle cx="13" cy="13" r="6" fill="none" stroke="#fff" stroke-width="1.5"/><path d="M7 13h12M13 7c-3 3.5-3 8.5 0 12M13 7c3 3.5 3 8.5 0 12" fill="none" stroke="#fff" stroke-width="1.2"/></svg>
      WWW.THECORNERSTONEFIXERS.COM
    </li>
  </ul>
  <div class="badge-text">WE SOLVE<br>ALL YOUR<br>REPAIR NEEDS<span class="badge-sub">Dwelling &amp; Lodging</span></div>
</section>

</body>
</html>
```